Velvet Pressings Techno Label Business Card

I'm looking for a very clean business card for my Velvet Pressings music label. The label focusses on techno music. The card should include:

• my name : Bram Quintel as "Founder & CEO"
• email address: bram@velvet-pressings.example
• web: www.velvet-pressings.example
• facebook logo + /velvetpress
• twitter logo + /velvetpress
• soundcloud logo + /velvetpressings

Feel free to include your ideas! I'm looking forward to discuss about it.

Bram

Industry/Entity Type

Business

Contact Information for Business Card

I don't like glossy cards. Prefer matt.

Requirements
Nice to have
• Maybe on one side the complete logo, other side just the icon.
Should not have
• Flashy stuff. Must be clean and business like style.

```html
<!DOCTYPE html>
<html lang="en">
<head>
<meta charset="utf-8">
<title>Velvet Pressings – Business Card</title>
<link rel="stylesheet" href="https://fonts.googleapis.com/css2?family=Lato:wght@300;400;700&display=swap">
<style>
  :root {
    --bg: #e9e6e1;
    --card: #fbfbfb;
    --card-edge: #e2e2e2;
    --orange: #ee7a3a;
    --grey-dark: #9a9a9a;
    --grey-mid: #a8a8a8;
    --grey-light: #b4b4b4;
  }
  * { box-sizing: border-box; margin: 0; padding: 0; }
  html, body {
    width: 1200px; height: 1023px; overflow: hidden;
    background: var(--bg);
    font-family: "Lato", sans-serif;
  }
  .canvas { position: relative; width: 1200px; height: 1023px; }
  .card {
    position: absolute;
    background: linear-gradient(160deg, #ffffff 0%, var(--card) 60%, #f1f1f1 100%);
    border-radius: 18px;
    box-shadow: 0 2px 0 var(--card-edge), 0 4px 0 #d8d8d8, 0 14px 30px rgba(0,0,0,0.18);
  }
  .card--front { left: 83px; top: 211px; width: 620px; height: 354px; }
  .card--back  { left: 763px; top: 200px; width: 354px; height: 620px; }

  .brand { position: absolute; display: flex; align-items: center; gap: 14px; white-space: nowrap; }
  .brand__square { width: 22px; height: 22px; background: var(--orange); flex: none; }
  .brand__name { font-weight: 700; color: var(--orange); letter-spacing: -0.5px; }
  .card--front .brand { left: 44px; top: 46px; }
  .card--front .brand__name { font-size: 44px; }

  .person { position: absolute; left: 44px; bottom: 48px; white-space: nowrap; }
  .person__name { font-size: 22px; font-weight: 700; color: var(--grey-dark); }
  .person__role { font-size: 20px; font-weight: 300; color: var(--grey-light); margin-top: 2px; }

  .contacts { position: absolute; left: 300px; bottom: 44px; list-style: none; }
  .contacts li {
    display: flex; align-items: center; gap: 10px;
    font-size: 15px; font-weight: 400; color: var(--grey-mid);
    line-height: 24px; white-space: nowrap;
  }
  .contacts .icon { width: 13px; height: 13px; flex: none; background: var(--orange); border-radius: 2px; }
  .contacts .icon--outline { background: none; border: 1.5px solid var(--grey-mid); }
  .contacts svg { flex: none; }

  .card--back .brand {
    left: 50%; top: 50%; transform: translate(-50%, -50%);
  }
  .card--back .brand__name { font-size: 34px; }
</style>
</head>
<body>
<main class="canvas">
  <section class="card card--front" aria-label="Card front">
    <div class="brand">
      <span class="brand__square"></span>
      <span class="brand__name">Velvet Pressings</span>
    </div>
    <div class="person">
      <p class="person__name">Bram Quintel</p>
      <p class="person__role">Founder &amp; CEO</p>
    </div>
    <ul class="contacts">
      <li>
        <svg width="13" height="13" viewBox="0 0 13 13" aria-hidden="true">
          <rect x="0" y="1.5" width="13" height="10" rx="1" fill="var(--orange)"/>
          <polyline points="0.5,2.5 6.5,7.5 12.5,2.5" fill="none" stroke="#fff" stroke-width="1.3"/>
        </svg>
        bram@velvet-pressings.example
      </li>
      <li><span class="icon icon--outline"></span>www.velvet-pressings.example</li>
      <li><span class="icon"></span>/velvetpress</li>
      <li><span class="icon"></span>/velvetpress</li>
      <li><span class="icon"></span>/velvetpressings</li>
    </ul>
  </section>

  <section class="card card--back" aria-label="Card back">
    <div class="brand">
      <span class="brand__name">Velvet Pressings</span>
    </div>
  </section>
</main>
</body>
</html>
```